Brennick Capital Business Cards

These are professional business cards that are for my family office.
Put fake emails and phone numbers as of now until I finalize those components. This family office controls my families investments, assets, and future. The cards should be professional.
..
.
.
.
I just uploaded another variation of a logo I would like to see as a business card to I am inbeteen which logo to use

Target Market(s)

business

Industry/Entity Type

business

Contact Information for Business Card

Professional, wealth related, finance related.

Requirements
Must have
• Logo

```html
<!DOCTYPE html>
<html lang="en">
<head>
<meta charset="utf-8">
<title>Brennick Capital Business Cards</title>
<link href="https://fonts.googleapis.com/css2?family=Cinzel:wght@500;700&family=Montserrat:wght@600&family=Arimo&display=swap" rel="stylesheet">
<style>
  :root {
    --backdrop: #ababab;
    --navy: #1c1f2b;
    --white: #ffffff;
    --grey: #a9a9a9;
    --text-dark: #2b2b2b;
    --title-grey: #3d3d3d;
  }
  * { margin: 0; padding: 0; box-sizing: border-box; }
  html, body { width: 1200px; height: 1000px; overflow: hidden; }
  body { background: var(--backdrop); position: relative; }

  .card { position: absolute; left: 207px; width: 786px; height: 450px; overflow: hidden; }
  .card--front { top: 40px; background: var(--navy); color: var(--white); }
  .card--back { top: 510px; background: var(--white); color: var(--navy); }

  .brand-ring { position: absolute; border-radius: 50%; }
  .card--front .brand-ring { left: 273px; top: 68px; width: 246px; height: 246px; border: 5px solid var(--white); }
  .brand-name { position: absolute; font-family: "Cinzel", serif; font-weight: 500; white-space: nowrap; text-align: center; }
  .card--front .brand-name { left: 0; width: 786px; top: 322px; font-size: 36px; color: var(--white); }
  .tagline { position: absolute; left: 0; width: 786px; top: 398px; text-align: center; font-family: "Arimo", sans-serif; font-size: 19px; letter-spacing: 3.6px; }

  .person-name { position: absolute; left: 38px; top: 86px; font-family: "Cinzel", serif; font-weight: 700; font-size: 28px; letter-spacing: 0.5px; color: var(--navy); }
  .person-title { position: absolute; left: 38px; top: 128px; font-family: "Montserrat", sans-serif; font-weight: 600; font-size: 20px; color: var(--title-grey); letter-spacing: 0.3px; }
  .title-rule { position: absolute; left: 38px; top: 163px; width: 50px; height: 3px; background: var(--navy); }

  .contact-list { position: absolute; left: 39px; top: 209px; list-style: none; font-family: "Arimo", sans-serif; font-size: 20px; color: var(--text-dark); }
  .contact-list li { display: flex; align-items: flex-start; height: 31.5px; line-height: 26px; }
  .contact-list li.address { height: auto; line-height: 31px; }
  .contact-icon { width: 22px; height: 22px; margin-right: 11px; margin-top: 2px; flex: none; }

  .card--back .brand-ring { left: 515px; top: 115px; width: 158px; height: 158px; border: 4px solid var(--navy); }
  .card--back .brand-name { left: 431px; width: 320px; top: 291px; font-size: 31px; color: var(--navy); }

  .footer-band { position: absolute; top: 402px; height: 22px; }
  .footer-band--dark { left: 0; width: 562px; background: var(--navy); }
  .footer-band--light { left: 624px; width: 162px; background: var(--grey); }
  .footer-seal { position: absolute; left: 560px; top: 383px; width: 60px; height: 60px; border-radius: 50%; background: var(--white); border: 3px solid var(--navy); }
</style>
</head>
<body>

<section class="card card--front">
  <div class="brand-ring"></div>
  <div class="brand-name">Brennick Capital</div>
  <p class="tagline">PRUDENT STEWARDSHIP. ENDURING LEGACY.</p>
</section>

<section class="card card--back">
  <h1 class="person-name">MARCUS ELLERY</h1>
  <p class="person-title">MANAGING DIRECTOR</p>
  <div class="title-rule"></div>

  <ul class="contact-list">
    <li>
      <svg class="contact-icon" viewBox="0 0 22 22"><rect width="22" height="22" rx="4" fill="#1c1f2b"/><path d="M7 5h3l1 4-2 1a9 9 0 0 0 3 3l1-2 4 1v3c0 1-1 2-2 2A11 11 0 0 1 5 7c0-1 1-2 2-2z" fill="#fff"/></svg>
      <span>044-555 018 240</span>
    </li>
    <li>
      <svg class="contact-icon" viewBox="0 0 22 22"><rect width="22" height="22" rx="4" fill="#1c1f2b"/><path d="M4 11 18 4l-4 14-3-5-7-2z" fill="#fff"/></svg>
      <span>office@brennickcap.com</span>
    </li>
    <li>
      <svg class="contact-icon" viewBox="0 0 22 22"><rect width="22" height="22" rx="4" fill="#1c1f2b"/><circle cx="11" cy="11" r="6" fill="none" stroke="#fff" stroke-width="1.6"/><path d="M5 11h12M11 5c-3 3-3 9 0 12M11 5c3 3 3 9 0 12" fill="none" stroke="#fff" stroke-width="1.3"/></svg>
      <span>www.brennickcap.com</span>
    </li>
    <li class="address">
      <svg class="contact-icon" viewBox="0 0 22 22"><rect width="22" height="22" rx="4" fill="#1c1f2b"/><path d="M11 4a5 5 0 0 0-5 5c0 4 5 9 5 9s5-5 5-9a5 5 0 0 0-5-5z" fill="#fff"/><circle cx="11" cy="9" r="2" fill="#1c1f2b"/></svg>
      <span>4410 Harbor Crest Pkwy,<br>210-B, FL 32541</span>
    </li>
  </ul>

  <div class="brand-ring"></div>
  <div class="brand-name">Brennick Capital</div>

  <div class="footer-band footer-band--dark"></div>
  <div class="footer-band footer-band--light"></div>
  <div class="footer-seal"></div>
</section>

</body>
</html>
```